riverstonelightcare - healing business promotion

I have and energy / intuitive healing and kinesiology business. working with people who are looking for healing outside of the modern medical model, who have tried but failed in their search for understanding their conditions and why health and or happiness eludes them. the healing is done with love, patience and understanding. I am looking to be taken seriously with my presentation and to reach a person who may be deterred by the thought of angels and intuition! but to not exclude those that are attracted to that also.

Industry/Entity Type

Medical

Contact Information for Business Card

riverstonelightcare
calm clear gentle energy renewal method
tamsin corrine hale
energy healing / kinesiology and neurotraining
0417362815 07 4186 2751
home visits available for cairns and tablelands
t.chale@maildrop-example.net

Requirements
Should not have
• Primary colours

```html
<!DOCTYPE html>
<html lang="en">
<head>
<meta charset="utf-8">
<title>riverstonelightcare – business card</title>
<link rel="stylesheet" href="https://fonts.googleapis.com/css2?family=EB+Garamond:ital,wght@0,400;0,600;1,400&display=swap">
<style>
  :root {
    --paper: #ffffff;
    --ink-navy: #17087f;
    --ink-grey: #3d3d3d;
    --ink-dark: #2a2a2a;
    --blossom: #fcd2fb;
    --blossom-soft: rgba(252, 210, 251, 0);
  }
  html, body {
    margin: 0;
    padding: 0;
    width: 1200px;
    height: 691px;
    overflow: hidden;
    background: var(--paper);
  }
  .card {
    position: relative;
    width: 1200px;
    height: 691px;
    overflow: hidden;
    background: var(--paper);
    font-family: "EB Garamond", Georgia, serif;
  }
  .floral-backdrop {
    position: absolute;
    left: 380px;
    top: 120px;
    width: 744px;
    height: 530px;
  }
  .brand {
    position: absolute;
    left: 0;
    width: 1120px;
    top: 118px;
    margin: 0;
    text-align: center;
    font-weight: 400;
    font-size: 66px;
    line-height: 1;
    color: var(--ink-navy);
    letter-spacing: 1px;
  }
  .tagline {
    position: absolute;
    left: 0;
    width: 1120px;
    top: 210px;
    margin: 0;
    text-align: center;
    font-size: 30px;
    letter-spacing: 3.2px;
    color: var(--ink-grey);
  }
  .practitioner {
    position: absolute;
    left: 0;
    width: 1120px;
    top: 322px;
    margin: 0;
    text-align: center;
    font-weight: 600;
    font-size: 40px;
    color: var(--ink-navy);
  }
  .modalities {
    position: absolute;
    left: 0;
    width: 1120px;
    top: 372px;
    margin: 0;
    text-align: center;
    font-style: italic;
    font-size: 27px;
    color: var(--ink-dark);
  }
  .contact {
    position: absolute;
    left: 0;
    width: 1120px;
    top: 424px;
    margin: 0;
    text-align: center;
    font-size: 27px;
    line-height: 44px;
    letter-spacing: 1.6px;
    color: var(--ink-navy);
    font-style: normal;
  }
  .contact span { display: block; }
  .service-area {
    position: absolute;
    left: 0;
    width: 1120px;
    top: 534px;
    margin: 0;
    text-align: center;
    font-size: 21px;
    font-variant: small-caps;
    text-transform: lowercase;
    letter-spacing: 1.6px;
    color: var(--ink-navy);
  }
</style>
</head>
<body>
  <main class="card">
    <svg class="floral-backdrop" viewBox="0 0 744 530" role="img" aria-label="Soft pink floral ornament of leaves, stems and blossoms">
      <defs>
        <radialGradient id="blossom-wash" cx="62%" cy="55%" r="60%">
          <stop offset="0%" stop-color="var(--blossom)" />
          <stop offset="60%" stop-color="var(--blossom)" stop-opacity="0.7" />
          <stop offset="100%" stop-color="var(--blossom)" stop-opacity="0" />
        </radialGradient>
      </defs>
      <rect x="0" y="0" width="744" height="530" fill="url(#blossom-wash)" />
    </svg>

    <h1 class="brand">riverstonelightcare</h1>
    <p class="tagline">calm, clear, gentle, energy renewal method</p>

    <h2 class="practitioner">Tamsin Corrine Hale</h2>
    <p class="modalities">energy healing / kinesiology and neurotraining</p>

    <address class="contact">
      <span>0417362815 07 4186 2751</span>
      <span>t.chale@maildrop-example.net</span>
    </address>

    <p class="service-area">Home visits available for Cairns and Tablelands</p>
  </main>
</body>
</html>
```